Wine Bottle Label for Tall Fern Cellars

We are a small, newly established winery in need of an original, bold and outstanding bottle label design for our Tall Fern wine.

Our vineyard and winery are located on a 200 acre farm in a remote part of southern Oregon. The name "Tall Fern" was inspired by the large, overgrown size of all of the foliage here, including our grapevines. Things grow large and vigorous in Oregon! And everything is very lush and green. It is almost surreal or other-worldly, like the landscapes seen in the Keeper of The Hollows movies, or the land of Yarrowmere. It is a place that makes you say "wow" with its epic, large scale, natural beauty.

The name "Tall Fern" also captures the essence of our wine. It is big in flavor, quality and color. Our first release is a Pinot Noir (red). Pinot Noir wines often are subtle in flavor and thin in their color. Our label should convey that our Pinot Noir is a much more robust, darker, heavier, meatier, more flavorful wine that is a lot more fun than an "ordinary" wine. At the same time, this wine is not cheap, and so nothing in the label should convey "bargain," "low price," or "cheapness." This is a fine wine with a sense of adventure. Be sure to convey "quality" with your design along with "big," "adventure" and "fun".

The label should appeal to a younger demographic, both male and female, between the ages of 21 and 35. It should be non-traditional and adventurous and suggest a pushing of boundaries and a breaking of rules. This Pinot Noir does not conform to the normal "limitations" of the variety, therefore the label should not conform. It should have an "organic" or "natural" or "agricultural" vibe, as opposed to something mechanical or technical. It should, however, be contemporary. Do not confuse "natural" or "organic" with being nostalgic or old school. Think "agri-hipsters."

The label should be designed to fit on a Burgundy-style wine bottle (photo attached for reference). (Note: All Pinot Noir and Chardonnay is bottled in Burgundy bottles, If you are not sure about the bottle shape you can go to a local store and compare the various bottles. Locate a bottle of Pinot Noir or Chardonnay or anything identified as a "Burgundy Wine," and it should be the correct bottle. The tall, skinny bottles used for Cabernet Sauvignon are NOT correct)). Please see the "Must Have" notes for more on the bottle.

In summary, the final project should be a wine bottle label design that conveys bigness, vastness, adventurous, non-traditional, high quality wine. A good tagline to keep in mind is "Living Large."

Target Market(s)

Young, hip, non-conformist wine drinkers aged 21-35 with a sense of adventure and an appreciation of quality.

Industry/Entity Type

School

Requirements
Must have
• *Must contain the words:

Tall Fern (the brand)
2013 Pinot Noir (the vintage year and variety)

*The label must be designed to fit a Burgundy-style wine bottle. A photo is attached for reference.

*Additionally, the label needs to fit on the lower, widest part of the bottle. The label will be printed on sticky paper and rolled onto the bottle with a machine. The machine cannot apply labels to the neck of the bottle. The maximum size of a label that will fit this space is 5.5 inches wide by 4.5 inches tall. You DO NOT have to fill ALL of this space or confine the label shape to a rectangle, but the label cannot exceed this size or it won't stick to the bottle properly. It will really help if you can put your hands on an actual bottle to see the logistics of applying the label. But if that is not possible, just do your best with the instructions you have. I am confident the winning design could be adjusted to fit the bottle, if necessary
Nice to have
• *Wine grape leaf or leaves.

*A concept I have been playing with is sunlight shining through leaves like light through a Kessler lamp or a stained glass window. This is NOT a requirement for this label. However, if the concept inspires and idea, I would be most happy to see it.
Should not have
• IF a leaf or leaves are included in the design (not a requirement) they MUST be wine grapevine leafs and preferably leaves of the Pinot Noir vine. Do not use generic leaves or identifiable leaves such as oak leaves, maple leaves, or anything that looks like the Canadian flag or the Dunmore Ice Hawks hockey logo. Reference the attached photos of wine grape leaves to see the correct leaf type. I am happy to email more photos upon request. These photos may be used in whole or in part in your design, however, a leaf from a photo is NOT a requirement, nor is the image of a leaf or leaves.

This label should NOT be designed for Bordeaux-style wine bottles (the tall, skinny ones).

```html
<!DOCTYPE html>
<html lang="en">
<head>
<meta charset="utf-8">
<title>Tall Fern Pinot Noir Label</title>
<link rel="stylesheet" href="https://fonts.googleapis.com/css2?family=Cinzel:wght@400;600&family=Crimson+Text:wght@400&display=swap">
<style>
  :root {
    --paper: #fffdf6;
    --ink: #15181a;
    --crimson: #e4104d;
    --band: #ff0a45;
    --blot-dark: #0b0a0d;
    --blot-plum: #5a2a66;
    --blot-rust: #9a4630;
    --blot-green: #2f4a3a;
  }
  html, body {
    margin: 0;
    padding: 0;
    overflow: hidden;
  }
  body {
    width: 1200px;
    height: 929px;
    background: var(--paper);
  }
  .label {
    position: relative;
    width: 1200px;
    height: 929px;
    background: var(--paper);
    overflow: hidden;
  }
  .label__artwork {
    position: absolute;
    left: 229px;
    top: 77px;
    width: 722px;
    height: 522px;
  }
  .label__brand {
    position: absolute;
    left: 0;
    right: 0;
    top: 630px;
    margin: 0;
    text-align: center;
    font-family: "Cinzel", serif;
    font-weight: 600;
    font-size: 98px;
    line-height: 1;
    letter-spacing: 2px;
    color: var(--ink);
  }
  .label__variety {
    position: absolute;
    left: 0;
    right: 0;
    top: 727px;
    margin: 0;
    text-align: center;
    font-family: "Cinzel", serif;
    font-weight: 400;
    font-size: 50px;
    line-height: 1;
    letter-spacing: 1px;
    color: var(--crimson);
  }
  .label__vintage {
    position: absolute;
    left: 0;
    right: 0;
    top: 778px;
    margin: 0;
    text-align: center;
    font-family: "Crimson Text", serif;
    font-size: 40px;
    line-height: 1;
    letter-spacing: 1px;
    color: var(--ink);
  }
  .label__band {
    position: absolute;
    left: 0;
    right: 0;
    top: 855px;
    height: 36px;
    background: var(--band);
  }
</style>
</head>
<body>
  <main class="label">
    <svg class="label__artwork" viewBox="0 0 722 522" role="img" aria-label="Large symmetrical watercolour grapevine leaf in deep black with plum, rust, yellow and green edges, flanked by small ink-spot grape clusters">
      <defs>
        <radialGradient id="blot-fill" cx="50%" cy="46%" r="50%">
          <stop offset="0%" stop-color="var(--blot-dark)"/>
          <stop offset="40%" stop-color="var(--blot-dark)"/>
          <stop offset="58%" stop-color="var(--blot-plum)" stop-opacity="0.85"/>
          <stop offset="72%" stop-color="var(--blot-rust)" stop-opacity="0.5"/>
          <stop offset="86%" stop-color="var(--blot-green)" stop-opacity="0.18"/>
          <stop offset="100%" stop-color="var(--paper)" stop-opacity="0"/>
        </radialGradient>
      </defs>
      <rect x="0" y="0" width="722" height="522" fill="url(#blot-fill)"/>
    </svg>

    <h1 class="label__brand">Tall Fern</h1>
    <p class="label__variety">Pinot Noir</p>
    <p class="label__vintage">2013</p>

    <div class="label__band"></div>
  </main>
</body>
</html>
```